website for outdoor advertising

to create a creative and friendly website illustrating our products; needs to show all our products and we are the largest outdoor advertising agency. its got to be clean and to the point and professional. it has to be user friendly, easy to navigate through the website, easy on the eye. not a lot of text.

Target Market(s)

potential companies looking to for outdoor advertising

Industry/Entity Type

Advertising

Coding

Coded - Design and coding required

Number of Pages Required

5+ page

Requirements
Nice to have
• http://www.tarvenquist.co.nz/ is a very nice website (the homepage style)

```html
<!DOCTYPE html>
<html lang="en">
<head>
<meta charset="utf-8">
<title>Halvero — Our Products</title>
<link rel="stylesheet" href="https://fonts.googleapis.com/css2?family=Source+Sans+3:wght@400;600&display=swap">
<style>
  :root {
    --page-bg: #ffffff;
    --rule-grey: #c9ccd1;
    --header-start: #2c6ea4;
    --header-mid: #24467e;
    --header-end: #1e2350;
    --nav-text: #ffffff;
    --nav-active: #9fd3f2;
    --nav-active-bg: rgba(255,255,255,0.08);
    --menu-bg: rgba(236,238,240,0.88);
    --menu-text: #4a4f57;
    --menu-line: #c4c8cd;
    --menu-hover: #7fa2cf;
    --heading-blue: #1b9ad6;
    --body-grey: #7a7d82;
    --card-bg: #ffffff;
    --card-band: #a8aaad;
    --button-top: #2f6fb8;
    --button-bottom: #174a8c;
    --icon-red: #e31e24;
    --icon-blue: #1a73b8;
    --icon-orange: #f15a24;
  }
  * { box-sizing: border-box; margin: 0; padding: 0; }
  html, body { width: 1200px; height: 900px; overflow: hidden; background: var(--page-bg); }
  body { font-family: "Source Sans 3", "Myriad Pro", sans-serif; position: relative; }

  .top-rule { position: absolute; left: 0; top: 54px; width: 1200px; height: 9px; background: var(--rule-grey); }

  .site-header {
    position: absolute; left: 0; top: 67px; width: 1200px; height: 104px;
    background: linear-gradient(90deg, var(--header-start) 0%, var(--header-mid) 55%, var(--header-end) 100%);
    box-shadow: 0 3px 6px rgba(0,0,0,0.25);
  }
  .brand-name {
    position: absolute; left: 127px; top: 26px;
    font-size: 46px; font-weight: 400; color: var(--nav-text); letter-spacing: 1px;
  }
  .search-field {
    position: absolute; left: 840px; top: 20px; width: 280px; height: 25px;
    background: rgba(255,255,255,0.22); border-radius: 3px;
  }
  .search-field svg { position: absolute; right: 6px; top: 4px; }

  .main-nav { position: absolute; top: 62px; left: 0; width: 1200px; height: 42px; }
  .main-nav a {
    position: absolute; top: 0; height: 42px; line-height: 40px;
    color: var(--nav-text); text-decoration: none; font-size: 19px;
  }
  .main-nav a.is-active {
    color: var(--nav-active); background: var(--nav-active-bg);
    width: 163px; text-align: center;
  }

  .dropdown {
    position: absolute; left: 528px; top: 171px; width: 163px; height: 184px;
    background: var(--menu-bg); list-style: none; padding-top: 4px; z-index: 5;
  }
  .dropdown li {
    height: 29.5px; line-height: 29px; padding-left: 28px;
    font-size: 16px; color: var(--menu-text);
    border-bottom: 1px solid var(--menu-line); margin: 0 6px 0 4px;
  }
  .dropdown li:last-child { border-bottom: none; }
  .dropdown li.is-hover { background: var(--menu-hover); color: #fff; margin: 0; padding-left: 32px; }

  .section-title {
    position: absolute; top: 245px; left: 0; width: 1200px; text-align: center;
    font-size: 37px; font-weight: 600; color: var(--heading-blue); letter-spacing: 0.5px;
  }
  .intro {
    position: absolute; top: 308px; left: 130px; width: 940px; text-align: center;
    font-size: 17px; line-height: 23px; color: var(--body-grey);
  }

  .product-card {
    position: absolute; top: 462px; width: 221px; height: 253px;
    background: var(--card-bg);
    box-shadow: 3px 4px 10px rgba(0,0,0,0.35);
  }
  .card-bravo { left: 170px; }
  .card-charlie { left: 496px; }
  .card-alpha { left: 817px; }
  .product-photo {
    position: absolute; left: 39px; top: 36px; width: 144px; height: 116px;
    border-radius: 50%; border: 2px solid #d9dadc;
  }
  .photo-bravo { background: radial-gradient(ellipse at 50% 40%, #f3e534 0%, #e2c714 45%, #2b2618 85%); }
  .photo-charlie { background: radial-gradient(ellipse at 50% 35%, #f2f3f6 0%, #6f78a4 35%, #1b1f3f 85%); }
  .photo-alpha { background: radial-gradient(ellipse at 50% 45%, #66b9e8 0%, #3a6d92 35%, #18223a 85%); }
  .detail-button {
    position: absolute; left: 51px; top: 173px; width: 120px; height: 20px;
    background: linear-gradient(var(--button-top), var(--button-bottom));
    border-radius: 2px; color: #fff; font-size: 9px; line-height: 20px; text-align: center;
  }
  .card-band {
    position: absolute; left: 0; bottom: 0; width: 100%; height: 30px;
    background: var(--card-band); color: #fff; font-size: 21px; line-height: 30px; text-align: center;
  }
  .card-icon {
    position: absolute; top: 665px; width: 66px; height: 66px; border-radius: 50%;
  }
  .icon-bravo { left: 135px; background: var(--icon-red); }
  .icon-charlie { left: 462px; background: var(--icon-blue); }
  .icon-alpha { left: 785px; background: var(--icon-orange); }
  .card-icon svg { position: absolute; left: 13px; top: 13px; }
</style>
</head>
<body>
  <div class="top-rule"></div>

  <header class="site-header">
    <div class="brand-name">Halvero</div>
    <div class="search-field">
      <svg width="18" height="18" viewBox="0 0 18 18"><circle cx="10" cy="7" r="5" fill="none" stroke="#fff" stroke-width="1.6"/><line x1="6.5" y1="10.5" x2="2" y2="15" stroke="#fff" stroke-width="1.8"/></svg>
    </div>
    <nav class="main-nav">
      <a href="#" style="left:445px">Home</a>
      <a href="#" class="is-active" style="left:528px">Our products</a>
      <a href="#" style="left:719px">Info and stats</a>
      <a href="#" style="left:888px">Map</a>
      <a href="#" style="left:973px">Contact us</a>
    </nav>
  </header>

  <ul class="dropdown">
    <li>Bravo</li>
    <li>Charlie</li>
    <li class="is-hover">Alpha</li>
    <li>Bus Stop</li>
    <li>Txai</li>
    <li>Buses</li>
  </ul>

  <h1 class="section-title">OUR PRODUCTS</h1>
  <p class="intro">Our products assist brands to meet and engage with the population in public spaces from bus stops to landmark billboards. The sizeable quantity of our advertising sites and effective campaigns allow brands to cover a whole city with their message.</p>

  <article class="product-card card-bravo">
    <div class="product-photo photo-bravo" role="img" aria-label="Yellow Bravo billboard lit at night"></div>
    <div class="detail-button">Click For Detail</div>
    <div class="card-band">Bravo</div>
  </article>
  <article class="product-card card-charlie">
    <div class="product-photo photo-charlie" role="img" aria-label="Blank roadside billboard at dusk"></div>
    <div class="detail-button">Click For Detail</div>
    <div class="card-band">Charlie</div>
  </article>
  <article class="product-card card-alpha">
    <div class="product-photo photo-alpha" role="img" aria-label="Illuminated Alpha street poster panel at night"></div>
    <div class="detail-button">Click For Detail</div>
    <div class="card-band">Alpha</div>
  </article>

  <div class="card-icon icon-bravo">
    <svg width="40" height="40" viewBox="0 0 40 40"><rect x="3" y="7" width="34" height="18" fill="none" stroke="#fff" stroke-width="3"/><line x1="12" y1="25" x2="12" y2="36" stroke="#fff" stroke-width="3"/><line x1="28" y1="25" x2="28" y2="36" stroke="#fff" stroke-width="3"/></svg>
  </div>
  <div class="card-icon icon-charlie">
    <svg width="40" height="40" viewBox="0 0 40 40"><rect x="3" y="7" width="34" height="20" fill="none" stroke="#fff" stroke-width="3"/><line x1="20" y1="27" x2="20" y2="37" stroke="#fff" stroke-width="3"/></svg>
  </div>
  <div class="card-icon icon-alpha">
    <svg width="40" height="40" viewBox="0 0 40 40"><rect x="9" y="4" width="22" height="31" fill="none" stroke="#fff" stroke-width="3"/><rect x="13" y="8" width="14" height="20" fill="#fff"/></svg>
  </div>
</body>
</html>
```